Bramwick Client Journey To Success

I need a one-page document that graphically shows the client's journey working with Bramwick from initial assessment to completed project. I want the journey to start at the "basecamp logo" and reach 4 summits (little mountain logos...) .

I'd like the imagery to convey the client starting at basecamp, and moving to each summit. Each summit, should list the subtext under each, as listed on the pdf doc i provided.

The description for the basecamp and 4 summits is attached.

I need the brochure to look like the other brochure that you did for me (attached) .

Target Market(s)

Restaurant Owners

Industry/Entity Type

Construction Management

Font styles to use
Sans Serif

Colors
EB3D1F
EC4F4E
F09395
F8D3D4
FCEDEE

Requirements
Must have
• My logo. Title: Client Journey To Success. Subtitle: The 4 Summits

```html
<!DOCTYPE html>
<html lang="en">
<head>
<meta charset="utf-8">
<title>Bramwick – Client Journey To Success</title>
<link href="https://fonts.googleapis.com/css2?family=Montserrat:wght@400;500;700;800;900&display=swap" rel="stylesheet">
<style>
  :root{
    --red:#d42b2b;
    --red-bright:#eb3d1f;
    --red-dark:#a81c22;
    --pink:#f09395;
    --pink-light:#f8d3d4;
    --ink:#1c1c1c;
    --text:#333333;
    --paper:#ffffff;
  }
  *{margin:0;padding:0;box-sizing:border-box}
  html,body{width:944px;height:1200px;overflow:hidden;background:var(--paper)}
  body{font-family:"Montserrat",Arial,sans-serif;color:var(--text)}
  .page{position:relative;width:944px;height:1200px;overflow:hidden;background:var(--paper)}

  .backdrop{position:absolute;left:0;top:0}

  .title{position:absolute;left:73px;top:44px;font-weight:900;font-size:29px;letter-spacing:.3px;color:var(--ink)}
  .title-rule{position:absolute;left:73px;top:84px;width:459px;height:2px;background:var(--red)}
  .title-rule::before{content:"";position:absolute;left:0;top:-2px;width:303px;height:6px;background:var(--ink)}
  .subtitle{position:absolute;left:73px;top:100px;font-weight:400;font-size:28px;color:var(--red)}

  .brand{position:absolute;left:738px;top:40px;width:150px;text-align:center}
  .brand-mark{width:96px;height:96px;margin:0 auto 22px;background:var(--red)}
  .brand-name{font-weight:800;font-size:13px;letter-spacing:.3px;color:var(--ink);white-space:nowrap;margin-left:-20px;margin-right:-20px}

  .stage{position:absolute;left:0;width:620px}
  .stage-hex{position:absolute;left:102px;width:120px;height:140px}
  .stage-copy{position:absolute;left:267px}
  .summit-tag{display:flex;flex-direction:column;align-items:flex-start;font-weight:800;font-size:13px;color:var(--red);line-height:1}
  .summit-tag svg{margin-bottom:3px}
  .stage-title{font-weight:800;font-size:21px;color:var(--ink);line-height:1.2}
  .steps{list-style:none;margin-top:5px}
  .steps li{position:relative;padding-left:12px;font-size:15px;line-height:24px;color:var(--text)}
  .steps li::before{content:"";position:absolute;left:0;top:10px;width:6px;height:6px;border-radius:50%;background:var(--red)}
</style>
</head>
<body>
<div class="page">

  <svg class="backdrop" width="944" height="1200" role="img" aria-label="Large soft pink decorative band along the right side">
    <defs>
      <linearGradient id="bandGrad" x1="0" y1="0" x2="1" y2="0">
        <stop offset="0" stop-color="#f4aaa9"/>
        <stop offset="1" stop-color="#e8a7aa"/>
      </linearGradient>
    </defs>
    <polygon points="563,492 944,270 944,1200 720,1200 563,1100" fill="url(#bandGrad)"/>
  </svg>

  <h1 class="title">CLIENT JOURNEY TO SUCCESS</h1>
  <div class="title-rule"></div>
  <p class="subtitle">The 4 Summits</p>

  <div class="brand">
    <div class="brand-mark"></div>
    <div class="brand-name">BRAMWICK DEVELOPMENT</div>
  </div>

  <svg width="0" height="0" style="position:absolute">
    <defs>
      <linearGradient id="hexGrad" x1="0" y1="0" x2="1" y2="1">
        <stop offset="0" stop-color="#e43a2e"/>
        <stop offset=".55" stop-color="#d42b2b"/>
        <stop offset="1" stop-color="#a81c22"/>
      </linearGradient>
      <symbol id="peak" viewBox="0 0 16 12">
        <polygon points="8,0 16,12 0,12" fill="#d42b2b"/>
        <polygon points="8,0 10.5,4 8,5.5 5.5,4" fill="#fff"/>
      </symbol>
    </defs>
  </svg>

  <!-- Basecamp -->
  <section class="stage" style="top:181px">
    <svg class="stage-hex" style="top:0" viewBox="0 0 120 140">
      <polygon points="60,0 120,35 120,105 60,140 0,105 0,35" fill="url(#hexGrad)"/>
      <g fill="#fff">
        <polygon points="60,40 92,98 68,98 60,82 52,98 28,98"/>
      </g>
      <g stroke="#fff" stroke-width="6" stroke-linecap="round">
        <line x1="44" y1="34" x2="54" y2="50"/><line x1="76" y1="34" x2="66" y2="50"/>
      </g>
    </svg>
    <div class="stage-copy" style="top:9px">
      <h2 class="stage-title">Basecamp</h2>
      <ul class="steps">
        <li>Client Assessment</li>
        <li>Determine Project Goals</li>
        <li>Proposal &amp; Fees</li>
      </ul>
    </div>
  </section>

  <!-- Summit 1 -->
  <section class="stage" style="top:356px">
    <svg class="stage-hex" style="top:0" viewBox="0 0 120 140">
      <polygon points="60,0 120,35 120,105 60,140 0,105 0,35" fill="url(#hexGrad)"/>
      <g fill="none" stroke="#fff" stroke-width="5">
        <rect x="26" y="46" width="68" height="22"/>
        <line x1="38" y1="68" x2="38" y2="100"/><line x1="82" y1="68" x2="82" y2="100"/>
        <line x1="38" y1="46" x2="38" y2="36"/><line x1="82" y1="46" x2="82" y2="36"/>
        <line x1="28" y1="100" x2="48" y2="100"/><line x1="72" y1="100" x2="92" y2="100"/>
      </g>
      <g stroke="#fff" stroke-width="6"><line x1="40" y1="66" x2="52" y2="48"/><line x1="58" y1="66" x2="70" y2="48"/><line x1="76" y1="66" x2="88" y2="48"/></g>
    </svg>
    <div class="stage-copy" style="top:17px">
      <div class="summit-tag"><svg width="18" height="13"><use href="#peak"/></svg>SUMMIT 1</div>
      <h2 class="stage-title">PreConstruction</h2>
      <ul class="steps">
        <li>Develop Project Plan</li>
        <li>Develop Risk Assessment &amp; Plan</li>
        <li>Devlelop Schedule</li>
        <li>Develop Budget</li>
        <li>Develop Team</li>
        <li>GC, Sub, Consultants Contracts</li>
      </ul>
    </div>
  </section>

  <!-- Summit 2 -->
  <section class="stage" style="top:603px">
    <svg class="stage-hex" style="top:0" viewBox="0 0 120 140">
      <polygon points="60,0 120,35 120,105 60,140 0,105 0,35" fill="url(#hexGrad)"/>
      <g stroke="#fff" stroke-width="4">
        <line x1="60" y1="70" x2="60" y2="36"/><line x1="60" y1="70" x2="60" y2="104"/>
        <line x1="60" y1="70" x2="30" y2="53"/><line x1="60" y1="70" x2="90" y2="53"/>
        <line x1="60" y1="70" x2="30" y2="87"/><line x1="60" y1="70" x2="90" y2="87"/>
      </g>
      <g fill="#d42b2b" stroke="#fff" stroke-width="4">
        <circle cx="60" cy="70" r="8"/>
        <circle cx="60" cy="34" r="6"/><circle cx="60" cy="106" r="6"/>
        <circle cx="28" cy="52" r="6"/><circle cx="92" cy="52" r="6"/>
        <circle cx="28" cy="88" r="6"/><circle cx="92" cy="88" r="6"/>
      </g>
    </svg>
    <div class="stage-copy" style="top:13px">
      <div class="summit-tag"><svg width="18" height="13"><use href="#peak"/></svg>SUMMIT 2</div>
      <h2 class="stage-title">Execution</h2>
      <ul class="steps">
        <li>Acquire Permits</li>
        <li>PreConstruction Meeting</li>
        <li>Project Start</li>
      </ul>
    </div>
  </section>

  <!-- Summit 3 -->
  <section class="stage" style="top:801px">
    <svg class="stage-hex" style="top:0" viewBox="0 0 120 140">
      <polygon points="60,0 120,35 120,105 60,140 0,105 0,35" fill="url(#hexGrad)"/>
      <g fill="none" stroke="#fff" stroke-width="5" stroke-linejoin="round">
        <polyline points="50,40 36,40 36,102 84,102 84,90"/>
        <polyline points="70,100 84,100"/>
        <polyline points="70,40 84,40 84,52"/>
        <line x1="48" y1="60" x2="72" y2="60"/><line x1="48" y1="72" x2="72" y2="72"/><line x1="48" y1="84" x2="64" y2="84"/>
      </g>
      <g fill="#fff"><polygon points="76,32 86,40 76,48"/><polygon points="44,94 34,102 44,110"/></g>
    </svg>
    <div class="stage-copy" style="top:-4px">
      <div class="summit-tag"><svg width="18" height="13"><use href="#peak"/></svg>SUMMIT 3</div>
      <h2 class="stage-title">Project Management</h2>
      <ul class="steps">
        <li>Shared Consciousness Meetings</li>
        <li>Pressurized Collaboration</li>
        <li>Schedule Management</li>
        <li>Run O.O.D.A. Loop</li>
      </ul>
    </div>
  </section>

  <!-- Summit 4 -->
  <section class="stage" style="top:977px">
    <svg class="stage-hex" style="top:0" viewBox="0 0 120 140">
      <polygon points="60,0 120,35 120,105 60,140 0,105 0,35" fill="url(#hexGrad)"/>
      <ellipse cx="50" cy="100" rx="22" ry="7" fill="none" stroke="#fff" stroke-width="4"/>
      <line x1="50" y1="100" x2="50" y2="36" stroke="#fff" stroke-width="5"/>
      <rect x="52" y="36" width="32" height="24" fill="#fff"/>
      <g fill="#d42b2b">
        <rect x="52" y="36" width="8" height="6"/><rect x="68" y="36" width="8" height="6"/>
        <rect x="60" y="42" width="8" height="6"/><rect x="76" y="42" width="8" height="6"/>
        <rect x="52" y="48" width="8" height="6"/><rect x="68" y="48" width="8" height="6"/>
        <rect x="60" y="54" width="8" height="6"/><rect x="76" y="54" width="8" height="6"/>
      </g>
    </svg>
    <div class="stage-copy" style="top:20px">
      <div class="summit-tag"><svg width="18" height="13"><use href="#peak"/></svg>SUMMIT 4</div>
      <h2 class="stage-title">Completion</h2>
      <ul class="steps">
        <li>Closeout</li>
      </ul>
    </div>
  </section>

</div>
</body>
</html>
```